Web-Design for Global Telecommunications Operator

We need a Wordpress web-site for our organisation "Vexlink" which is a B2B telecommunications operator with presence in Australia, Fiji, Papua New Guinea, UK, Singapore, Anguilla.

The company has multiple sides to it:
1) Carrier Wholesale - we provide international call termination to carriers globally of the likes of Marquon, KR, OP&L, Quenvo, Ramex, Soren Velacom.

2) Call Center Termination - we provide our network to call centers to be able to terminate their calls to the end user in order to perform telemarketing activities.

3) Satellite - we provide internet bandwidth via Satellite to customers from around the world

4) Consultancy - with over 35 years of experience under our belt, we believe we are fit to offer consultancy to people facing challenges within the IT&T industry.

5) B2C - Our operations globally also own various retail operations that market B2C services.

Our colours are red, white and black and we would like to stick to this theme.

Industry/Entity Type

Telecommunications

```html
<!DOCTYPE html>
<html lang="en">
<head>
<meta charset="utf-8">
<title>Vexlink — Global Telecommunications</title>
<link rel="stylesheet" href="https://fonts.googleapis.com/css2?family=Lato:wght@300;400;700&family=Patua+One&family=Roboto:wght@400;500&display=swap">
<style>
:root{
  --red:#e8121b;
  --red-deep:#c90d14;
  --white:#ffffff;
  --paper:#f8f8f8;
  --band:#eef0f3;
  --ink:#2b2b2b;
  --muted:#7a7a7a;
  --line:#e3e3e3;
  --black:#000000;
  --foot-text:#cfcfcf;
  --gold:#d9962c;
}
*{box-sizing:border-box;margin:0;padding:0}
html,body{width:682px;height:1200px;overflow:hidden}
body{position:relative;font-family:"Roboto",Arial,sans-serif;color:var(--ink);background:var(--paper)}
.abs{position:absolute}

/* hero */
.hero{left:0;top:0;width:682px;height:356px;background:radial-gradient(ellipse at 60% 45%,#f23a3f 0%,var(--red) 45%,var(--red-deep) 100%)}
.topbar{left:24px;top:11px;font-size:7px;color:#ffd2d4}
.topbar span{margin-right:10px}
.topbar .hidden-red{color:#f44a50}
.top-social{right:24px;top:11px;display:flex;gap:7px}
.top-social i,.bottom-social i{display:block;width:8px;height:8px;border-radius:50%;background:#f6888c}
.header{left:24px;top:33px;width:540px;height:47px;background:var(--white);box-shadow:0 2px 4px rgba(0,0,0,.15)}
.brand{left:8px;top:13px;display:flex;align-items:center;gap:6px;font-family:"Lato",sans-serif;font-weight:700;font-size:18px;color:var(--ink)}
.brand i{width:18px;height:18px;border-radius:50%;background:var(--red)}
.nav{right:0;top:0;height:47px;display:flex;font-size:8.5px;font-family:"Roboto",sans-serif}
.nav a{display:flex;align-items:center;padding:0 10px;color:var(--ink);text-decoration:none;border-left:1px solid #efefef}
.nav a:first-child{border-left:0}
.nav a.active{color:var(--red)}
.tools{left:566px;top:31px;width:89px;height:47px;background:var(--white);box-shadow:0 2px 4px rgba(0,0,0,.15)}
.badge{left:25px;top:13px;width:9px;height:9px;border-radius:2px;background:var(--red);color:#fff;font-size:5px;text-align:center;line-height:9px}
.flag{left:60px;top:17px;width:20px;height:14px;border:1px solid var(--line);border-radius:2px;background:#fff}
.flag i{position:absolute;left:4px;top:3px;width:10px;height:6px;background:linear-gradient(#2b3f8c,#2b3f8c 35%,#d22 35%,#d22 65%,#2b3f8c 65%)}
.hero-photo{left:332px;top:80px;width:241px;height:270px;background:radial-gradient(ellipse at 50% 55%,#4fd3ff 0%,#1f6f9a 25%,#233247 55%,rgba(35,50,71,0) 80%);border-radius:40% 40% 0 0}
.hero-copy{left:66px;top:164px;width:270px;font-family:"Lato",sans-serif;font-size:16.4px;line-height:25.5px;color:var(--white)}

/* services */
.services-title{left:0;top:386px;width:682px;text-align:center;font-family:"Lato",sans-serif;font-weight:300;font-size:23px;color:#444}
.service{top:450px;width:150px;text-align:center}
.service .ring{margin:0 auto;width:58px;height:58px;border-radius:50%;background:var(--white);box-shadow:0 0 0 4px #f1f1f1;display:flex;align-items:center;justify-content:center}
.service h3{margin-top:17px;font-family:"Lato",sans-serif;font-weight:400;font-size:11.5px;color:#555}
.service p{margin-top:8px;font-size:6.8px;line-height:11px;color:#666}

/* info columns */
.col{top:628px;width:205px}
.col h2{font-family:"Patua One",serif;font-weight:400;font-size:16px;color:var(--ink)}
.checks{list-style:none;margin-top:6px}
.checks li{display:flex;align-items:center;gap:10px;height:22px;font-size:8px;color:var(--muted);border-bottom:1px solid #ececec}
.checks li:last-child{border-bottom:0}
.col p{margin-top:8px;font-size:7.5px;line-height:12px;color:#555}
.col p.soft{color:#777;margin-top:6px}
.field-label{margin-top:8px;font-size:7.5px;color:#555}
.field{margin-top:7px;width:202px;height:21px;border:1px solid var(--line);background:var(--white)}
.btn{margin-top:6px;display:inline-block;padding:0 11px;height:21px;line-height:21px;border-radius:2px;background:var(--red);color:#fff;font-size:7.5px}

/* contact band */
.band{left:0;top:805px;width:682px;height:145px;background:var(--band)}
.band h2{position:absolute;left:0;top:30px;width:682px;text-align:center;font-family:"Patua One",serif;font-weight:400;font-size:15.5px;color:#333}
.contact{top:887px;display:flex;gap:18px;align-items:flex-start}
.contact small{display:block;font-size:7.5px;color:#666}
.contact strong{display:block;margin-top:5px;font-family:"Patua One",serif;font-weight:400;font-size:11px;color:#444}

/* footer */
.footer{left:0;top:950px;width:682px;height:250px;background:var(--black);color:var(--foot-text)}
.promo{position:absolute;left:0;top:17px;width:682px;text-align:center;font-size:10px;color:#ddd}
.promo em{font-style:normal;color:var(--red)}
.promo b{font-weight:400;color:#fff}
.fcol{position:absolute;top:64px;width:150px}
.fcol h4{font-family:"Patua One",serif;font-weight:400;font-size:11.5px;color:#fff}
.fbrand{display:flex;align-items:center;gap:6px;font-family:"Lato",sans-serif;font-weight:700;font-size:18px;color:#fff}
.fbrand i{width:18px;height:18px;border-radius:50%;background:#fff}
.fcol p{font-size:7.3px;line-height:11px;color:#ddd}
.fcol u{text-decoration:underline}
.squares{display:flex;gap:3px;margin-top:9px}
.squares i{width:25px;height:25px;background:#fff;display:flex;align-items:center;justify-content:center}
.squares i::after{content:"";width:7px;height:7px;border-radius:50%;background:#555}
.comment{position:relative;padding-left:25px;margin-top:12px;font-size:6.5px;line-height:11px}
.comment .dot{position:absolute;left:0;top:0;width:9px;height:9px;border-radius:50%;border:2px solid var(--red);background:#222}
.comment .date{color:#bbb}
.comment .who{color:#fff}
.comment .link{color:var(--red)}
.post{position:relative;height:48px;margin-top:10px;border-bottom:1px solid #222}
.post b{display:block;font-weight:500;font-size:6.8px;color:#fff}
.post span{display:block;margin-top:6px;font-size:6.5px;color:#bbb}
.thumb{position:absolute;right:0;top:-3px;width:45px;height:43px}
.count{position:absolute;right:-6px;bottom:6px;width:12px;height:12px;background:var(--red);color:#fff;font-size:6px;text-align:center;line-height:12px}
.feat{list-style:none;margin-top:6px}
.feat li{position:relative;padding:5px 0 5px 27px;font-size:7px;line-height:11px;color:#ddd;border-bottom:1px solid #1d1d1d}
.feat li svg{position:absolute;left:9px;top:6px}
.base{position:absolute;left:0;top:205px;width:682px;height:45px;border-top:1px solid #1c1c1c}
.base small{position:absolute;left:24px;top:19px;font-size:7px;color:#bbb}
.bottom-social{position:absolute;right:70px;top:20px;display:flex;gap:8px}
.bottom-social i{background:#555}
.totop{position:absolute;right:24px;top:10px;width:24px;height:24px;background:#fff;border-radius:2px;display:flex;align-items:center;justify-content:center}
</style>
</head>
<body>

<section class="hero abs">
  <div class="topbar abs"><span>Have any questions?</span><span class="hidden-red">+44 (0) 1 5550 2190</span><span class="hidden-red">info@vexlink.net</span></div>
  <div class="top-social abs"><i></i><i></i><i></i><i></i><i></i><i></i><i></i><i></i><i></i></div>

  <header class="header abs">
    <div class="brand abs"><i></i>Vexlink</div>
    <nav class="nav abs">
      <a class="active">Home</a><a>About Us</a><a>Services</a><a>Products</a><a>Other</a><a>Contact Us</a>
    </nav>
  </header>
  <div class="tools abs">
    <svg class="abs" style="left:14px;top:18px" width="12" height="11" viewBox="0 0 12 11"><path d="M0 1h2l2 6h6l1.5-4.5H3" fill="none" stroke="#333" stroke-width="1.3"/><circle cx="5" cy="9.5" r="1" fill="#333"/><circle cx="9" cy="9.5" r="1" fill="#333"/></svg>
    <div class="badge abs">0</div>
    <svg class="abs" style="left:40px;top:19px" width="10" height="10" viewBox="0 0 10 10"><circle cx="4" cy="4" r="3" fill="none" stroke="#333" stroke-width="1.4"/><path d="M6.2 6.2L9.2 9.2" stroke="#333" stroke-width="1.5"/></svg>
    <div class="flag abs"><i></i></div>
  </div>

  <div class="hero-photo abs" role="img" aria-label="Person in a dark coat holding a glowing globe of networked people in cupped hands"></div>
  <p class="hero-copy abs">Our organisation "Vexlink" which is a B2B telecommunications&nbsp; operator with presence in Australia, Fiji, Papua New Guinea, UK, Singapore, Anguilla.</p>
</section>

<h1 class="services-title abs">We will organize everything for you</h1>

<div class="service abs" style="left:22px">
  <div class="ring"><svg width="28" height="28" viewBox="0 0 28 28" fill="none" stroke="var(--gold)" stroke-width="1.6"><circle cx="18" cy="10" r="6"/><circle cx="19" cy="9" r="1.5"/><path d="M14 14L4 24M7 21l3 3M10 18l2 2"/></svg></div>
  <h3>Carrier Wholesale</h3>
  <p>we provide international call termination to carriers globally of the likes of Marquon, KR, OP&amp;L, Quenvo, Ramex, Soren Velacom.</p>
</div>
<div class="service abs" style="left:183px">
  <div class="ring"><svg width="28" height="28" viewBox="0 0 28 28" fill="none" stroke="var(--gold)" stroke-width="1.6"><rect x="3" y="8" width="22" height="15" rx="3"/><path d="M10 8l2-3h4l2 3"/><circle cx="14" cy="15.5" r="4.5"/></svg></div>
  <h3>Call Center Termination</h3>
  <p>we provide our network to call centers to be able to terminate their calls to the end user in order to perform telemarketing activities.</p>
</div>
<div class="service abs" style="left:345px">
  <div class="ring"><svg width="28" height="28" viewBox="0 0 28 28" fill="none" stroke="var(--gold)" stroke-width="1.6"><circle cx="8" cy="21" r="3.5"/><circle cx="20" cy="19" r="3.5"/><path d="M11.5 21V6l12-2v15M11.5 10l12-2"/></svg></div>
  <h3>Consultancy</h3>
  <p>over 35 years of experience under our belt, we believe we are fit to offer consultancy to people facing challenges within the IT&amp;T industry.</p>
</div>
<div class="service abs" style="left:506px">
  <div class="ring"><svg width="28" height="28" viewBox="0 0 28 28" fill="none" stroke="var(--gold)" stroke-width="1.6"><path d="M3 14h22c0 5-4 9-11 9S3 19 3 14zM6 14c0-3 3-5 8-5s8 2 8 5M10 6c0-1.5 1-1.5 1-3M14 6c0-1.5 1-1.5 1-3M18 6c0-1.5 1-1.5 1-3"/></svg></div>
  <h3>B2C</h3>
  <p>Our operations globally also own various retail operations that market B2C services.</p>
</div>

<div class="col abs" style="left:24px">
  <h2>How we do it?</h2>
  <ul class="checks">
    <li><svg width="10" height="8" viewBox="0 0 10 8"><path d="M1 4l3 3 5-6" fill="none" stroke="#222" stroke-width="1.6"/></svg>We sell all over the world.</li>
    <li><svg width="10" height="8" viewBox="0 0 10 8"><path d="M1 4l3 3 5-6" fill="none" stroke="#222" stroke-width="1.6"/></svg>Satisfaction or money refund guaranteed.</li>
    <li><svg width="10" height="8" viewBox="0 0 10 8"><path d="M1 4l3 3 5-6" fill="none" stroke="#222" stroke-width="1.6"/></svg>Lifetime updates &amp; support.</li>
    <li><svg width="10" height="8" viewBox="0 0 10 8"><path d="M1 4l3 3 5-6" fill="none" stroke="#222" stroke-width="1.6"/></svg>24 hours shipping.</li>
    <li><svg width="10" height="8" viewBox="0 0 10 8"><path d="M1 4l3 3 5-6" fill="none" stroke="#222" stroke-width="1.6"/></svg>We provide best tools ever.</li>
  </ul>
</div>
<div class="col abs" style="left:238px">
  <h2>About Vexlink</h2>
  <p>our organisation "Vexlink" which is a B2B telecommunications operator with presence in Australia, Fiji, Papua New Guinea, UK, Singapore, Anguilla.</p>
  <p class="soft">Aenean ligula nibh, molestie id viverra a, dapibus at dolor. In iaculis viverra neque, ac eleifend ante lobortis id. In viverra ipsum ac eros tristique dignissim. DonVitae adipiscing turpis. Aen</p>
</div>
<div class="col abs" style="left:453px">
  <h2>Newsletter</h2>
  <p>If you want to receive messages with latest updates, newest products and outstanding tools, please do not forget to give your e-mail address below</p>
  <div class="field-label">Put your e-mail address:</div>
  <div class="field"></div>
  <span class="btn">Subscribe</span>
</div>

<section class="band abs">
  <h2>Stay in touch with us</h2>
</section>
<div class="contact abs" style="left:31px">
  <svg width="28" height="20" viewBox="0 0 28 20" fill="none" stroke="var(--red)" stroke-width="1.6"><rect x="1" y="1" width="26" height="18"/><path d="M1 1l13 10L27 1M1 19l10-9M27 19l-10-9"/></svg>
  <div><small>Have any questions?</small><strong>info@vexlink.net</strong></div>
</div>
<div class="contact abs" style="left:246px">
  <svg width="28" height="24" viewBox="0 0 28 24" fill="none" stroke="var(--red)" stroke-width="1.6"><ellipse cx="14" cy="10" rx="12.5" ry="8.5"/><path d="M8 17l-3 6 8-5"/></svg>
  <div><small>Call us</small><strong>+44 (0) 1 5550 2190</strong></div>
</div>
<div class="contact abs" style="left:461px">
  <svg width="26" height="26" viewBox="0 0 26 26" fill="none" stroke="var(--red)" stroke-width="1.6"><rect x="5" y="1" width="20" height="24"/><path d="M5 6H1v17a2 2 0 004 0M9 6h12M9 10h5M9 14h5M9 18h12M9 21h12"/><rect x="16" y="10" width="5" height="5"/></svg>
  <div><small>Fax</small><strong>+44 (0) 1 5550 2190</strong></div>
</div>

<footer class="footer abs">
  <p class="promo">If you are interested in <em>Neo</em><b>theme</b>, do not wait and <b>BUY IT NOW!</b></p>

  <div class="fcol" style="left:24px;top:56px;width:150px">
    <div class="fbrand"><i></i>Vexlink</div>
    <p style="margin-top:7px;font-size:7.5px">We love who we are and we are very proud to be the part of your business</p>
    <p style="margin-top:7px">Curabitur sit amet magna quam. Praesent in libero vel <u>turpis pellentesque</u> egestas sit amet vel nunc. Nunc lobortis dui neque quis.</p>
    <div class="squares"><i></i><i></i><i></i><i></i><i></i></div>
  </div>

  <div class="fcol" style="left:185px">
    <h4>Recent comments</h4>
    <div class="comment"><span class="dot"></span><div class="date">March 31, 2014</div><div><span class="who">Harbor Studio commented on</span> <span class="link">Content builder for posts</span></div></div>
    <div class="comment" style="margin-top:14px"><span class="dot"></span><div class="date">March 31, 2014</div><div><span class="who">Harbor Studio commented on</span> <span class="link">Content builder for posts</span></div></div>
  </div>

  <div class="fcol" style="left:353px;width:141px">
    <h4>Latest posts</h4>
    <div class="post"><b>Content builder for posts</b><span>May 13, 2014</span>
      <div class="thumb" role="img" aria-label="Photo of a person with blonde hair" style="background:linear-gradient(135deg,#e8d2b6,#c79a6e)"><span class="count">5</span></div></div>
    <div class="post" style="border-bottom:0"><b>Post with vertical photo</b><span>May 13, 2014</span>
      <div class="thumb" role="img" aria-label="Photo of a person with curly dark hair" style="background:linear-gradient(135deg,#9a8b7c,#4a3e36)"><span class="count">0</span></div></div>
  </div>

  <div class="fcol" style="left:506px;width:152px">
    <h4>Some features</h4>
    <ul class="feat">
      <li><svg width="9" height="8" viewBox="0 0 9 8"><path d="M1 4l2.5 3L8 1" fill="none" stroke="#666" stroke-width="1.5"/></svg>Suspendisse a pellentesque dui, non felis.</li>
      <li><svg width="9" height="9" viewBox="0 0 10 10"><path d="M5 0l1.5 3.2 3.5.4-2.6 2.3.8 3.5L5 7.6 1.8 9.4l.8-3.5L0 3.6l3.5-.4z" fill="#666"/></svg>Quisque lorem tortor fringilla sed.</li>
      <li><svg width="9" height="9" viewBox="0 0 9 9"><circle cx="4.5" cy="3.5" r="3" fill="none" stroke="#666" stroke-width="1.2"/><path d="M3 8h3" stroke="#666" stroke-width="1.2"/></svg>Quisque cursus et, porttitor risus.</li>
      <li style="border-bottom:0"><svg width="9" height="8" viewBox="0 0 9 8"><path d="M1 4l2.5 3L8 1" fill="none" stroke="#666" stroke-width="1.5"/></svg>Nulla ipsum dolor lacus, suscipit.</li>
    </ul>
  </div>

  <div class="base">
    <small>© 2014 Vexlink. All Rights Reserved.</small>
    <div class="bottom-social"><i></i><i></i><i></i><i></i><i></i><i></i><i></i><i></i><i></i></div>
    <div class="totop"><svg width="8" height="5" viewBox="0 0 8 5"><path d="M1 4l3-3 3 3" fill="none" stroke="#555" stroke-width="1.2"/></svg></div>
  </div>
</footer>

</body>
</html>
```